professional business card design

Business card design. Photos have been uploaded and i am open to the designer choosing which photos to use. Would like the card to be mostyly in a grey scale design with black, whites, silver & grey colours. I have added copy of our flyer as would like on the back side of card our services to be listed. Do not use any bright colurs such as blue red green or yellow. i need to be able to edit the phone number and naem in the final card design submitted.

Target Market(s)

Clients

Industry/Entity Type

earhmovibng and transport

Contact Information for Business Card

Director Name, address, email, phone number and services

Colors

Designer to choose only greyscale colors for use in the design.

Requirements
Should not have
• no yellow, red, blue or green

```html
<!DOCTYPE html>
<html lang="en">
<head>
<meta charset="utf-8">
<title>Ridgeline Haulage – Business Card</title>
<link rel="stylesheet" href="https://fonts.googleapis.com/css2?family=Exo+2:wght@500;600;700&family=Michroma&display=swap">
<style>
  :root {
    --bg: #2a2320;
    --card: #050505;
    --panel-hi: #5a5a5a;
    --panel-mid: #2b2b2b;
    --silver: #e6e6e6;
    --silver-soft: #c8c8c8;
    --grey: #8a8a8a;
    --photo-hi: #9a9a9a;
  }
  * { margin: 0; padding: 0; box-sizing: border-box; }
  html, body { width: 1200px; height: 1200px; overflow: hidden; }
  body {
    background: var(--bg);
    display: flex;
    flex-direction: column;
    align-items: center;
    justify-content: center;
    gap: 56px;
    font-family: "Exo 2", sans-serif;
    color: var(--silver);
  }
  .card {
    position: relative;
    width: 900px;
    height: 514px;
    background: var(--card);
    overflow: hidden;
    box-shadow: 0 10px 30px rgba(0,0,0,.55);
  }

  /* Front */
  .front-panel {
    position: absolute;
    left: 150px; top: 0;
    width: 600px; height: 100%;
    background: radial-gradient(ellipse 60% 55% at 50% 42%, var(--panel-hi) 0%, var(--panel-mid) 55%, var(--card) 100%);
  }
  .brand {
    position: absolute;
    top: 70px; left: 0; right: 0;
    text-align: center;
  }
  .brand-name {
    font-weight: 700;
    font-size: 40px;
    letter-spacing: 2px;
    color: var(--silver);
  }
  .brand-sub {
    display: block;
    font-weight: 600;
    font-size: 14px;
    letter-spacing: 3px;
    color: var(--grey);
    margin-top: 2px;
  }
  .fleet-photo {
    position: absolute;
    left: 190px; top: 170px;
    width: 520px; height: 120px;
    background: radial-gradient(ellipse 70% 60% at 50% 60%, var(--photo-hi) 0%, #3a3a3a 55%, rgba(0,0,0,0) 100%);
  }
  .person {
    position: absolute;
    top: 310px; left: 0; right: 0;
    text-align: center;
  }
  .person-name {
    font-family: "Michroma", sans-serif;
    font-size: 52px;
    letter-spacing: 4px;
    color: var(--silver);
  }
  .person-role {
    font-family: "Michroma", sans-serif;
    font-size: 18px;
    letter-spacing: 2px;
    color: var(--silver-soft);
    margin-top: 6px;
  }
  .contact {
    position: absolute;
    top: 440px; left: 0; right: 0;
    display: flex;
    justify-content: center;
    gap: 34px;
    font-family: "Michroma", sans-serif;
    font-size: 16px;
    letter-spacing: 2px;
    color: var(--silver);
  }
  .contact-item { display: flex; align-items: center; gap: 10px; }
  .contact-item svg { width: 22px; height: 22px; }

  /* Back */
  .truck-photo {
    position: absolute;
    left: 80px; top: 40px;
    width: 620px; height: 430px;
    background: radial-gradient(ellipse 55% 55% at 45% 55%, #5c5c5c 0%, #2a2a2a 55%, rgba(0,0,0,0) 100%);
  }
  .services-title {
    position: absolute;
    top: 34px; left: 0; right: 0;
    text-align: center;
    font-weight: 700;
    font-size: 46px;
    line-height: 56px;
    letter-spacing: 1px;
    color: var(--silver);
    padding-left: 40px;
  }
  .service-list {
    position: absolute;
    list-style: none;
    font-weight: 600;
    font-size: 24px;
    line-height: 30px;
    color: var(--silver);
  }
  .service-list li::before { content: "• "; }
  .service-list.primary { top: 110px; left: 50px; }
  .service-list.fleet { top: 140px; left: 520px; }
  .service-list .indent { padding-left: 14px; }
  .service-list .indent::before { content: ""; }
  .cta {
    position: absolute;
    top: 338px; left: 0; right: 0;
    text-align: center;
    font-weight: 700;
    font-size: 26px;
    line-height: 31px;
    color: var(--silver);
    padding-left: 60px;
  }
  .cta-phone {
    position: absolute;
    top: 404px; left: 0; right: 0;
    text-align: center;
    font-weight: 700;
    font-size: 62px;
    line-height: 74px;
    color: var(--silver);
  }
</style>
</head>
<body>

  <section class="card card-front">
    <div class="front-panel"></div>
    <div class="brand">
      <span class="brand-name">RIDGELINE</span>
      <span class="brand-sub">HAULAGE PTY LTD</span>
    </div>
    <div class="fleet-photo" role="img" aria-label="Road train with side tipper trailers at a work site"></div>
    <div class="person">
      <div class="person-name">JOHN DOE</div>
      <div class="person-role">DIRECTOR</div>
    </div>
    <div class="contact">
      <span class="contact-item">
        <svg viewBox="0 0 24 24" fill="none" stroke="currentColor" stroke-width="1.6" aria-hidden="true">
          <circle cx="12" cy="12" r="10.5"/>
          <path d="M8.5 7.5c-.6.6-.8 1.8.2 3.6 1 1.8 2.6 3.4 4.3 4.2 1.6.8 2.6.5 3.1 0l.6-.7-2-1.6-1 .9c-.9-.3-2.3-1.7-2.7-2.6l.9-1-1.6-2.1z" fill="currentColor" stroke="none"/>
        </svg>
        04 321 876
      </span>
      <span class="contact-item">
        <svg viewBox="0 0 24 24" fill="none" stroke="currentColor" stroke-width="1.6" aria-hidden="true">
          <circle cx="12" cy="12" r="10.5"/>
          <rect x="6.5" y="8" width="11" height="8" rx="1"/>
          <path d="M6.8 8.5 12 12.6l5.2-4.1"/>
        </svg>
        OFFICE@RIDGELINEHAUL.COM
      </span>
    </div>
  </section>

  <section class="card card-back">
    <div class="truck-photo" role="img" aria-label="Front view of a prime mover hauling a road train"></div>
    <h2 class="services-title">OUR SERVICES</h2>
    <ul class="service-list primary">
      <li>Over size loads / Hot Shot Loads</li>
      <li>Heavy Vehicle Recovery Services</li>
      <li>Potable Water Deliveries</li>
      <li>Road Building / Maintainance</li>
      <li>Earthworks</li>
      <li>Sand &amp; Metal Supply &amp; Cartage</li>
    </ul>
    <ul class="service-list fleet">
      <li>Road Train Tippers</li>
      <li>Road Train Tankers</li>
      <li>Road Train Flat Tops</li>
      <li>Drop Deck Trailers</li>
      <li>Mine Site accredited</li>
      <li class="indent">equipment &amp; Operatoins</li>
    </ul>
    <p class="cta">Call us today for a personalised<br>quote to suit your needs.</p>
    <p class="cta-phone">04 321 876</p>
  </section>

</body>
</html>
```